Business Card and Stationary Designs for commercial construction company
Halvern Builders, Inc.
Creative Brief
Use standard fonts
Dennis Whitlock
Director of Operations
6387 Larkmeadow Lane Elk Grove, CA 95731
dennis.whitlock@halvernbldg.com
License #3084519
We like the colors of our logo, so please incorporate them into the card. The font for the other information on the business card does not have to match the logo font, but it should coordinate with it. We need the stationary design to be used to print actual stationary, but we would also like a word document that we can use for creating letters on electronic stationary.

```html
<!DOCTYPE html>
<html lang="en">
<head>
<meta charset="utf-8">
<title>Halvern Builders, Inc. – Business Card</title>
<link href="https://fonts.googleapis.com/css2?family=Montserrat:wght@500;600;800&display=swap" rel="stylesheet">
<style>
  :root {
    --brand-red: #e0262b;
    --brand-grey: #8a8c8f;
    --ink: #55575a;
    --card-white: #fbfbfb;
    --card-shade: #e9e9ea;
    --backdrop: #d9d6d2;
  }
  * { box-sizing: border-box; margin: 0; padding: 0; }
  html, body { width: 1200px; height: 901px; overflow: hidden; }
  body {
    background: var(--backdrop);
    font-family: "Montserrat", Arial, sans-serif;
    position: relative;
  }
  .business-card {
    position: absolute;
    left: 150px; top: 190px;
    width: 900px; height: 520px;
    border-radius: 56px;
    background: linear-gradient(160deg, var(--card-white) 0%, var(--card-shade) 100%);
    box-shadow: 0 18px 40px rgba(0,0,0,.18);
    overflow: hidden;
  }
  .card-swoosh { position: absolute; left: 0; bottom: 0; width: 900px; height: 520px; }
  .brand-name {
    position: absolute; left: 0; right: 0; top: 62px;
    text-align: center;
    font-weight: 800; font-size: 64px; letter-spacing: 4px;
    color: var(--brand-red);
  }
  .identity {
    position: absolute; right: 420px; top: 180px;
    text-align: right; font-variant: small-caps;
  }
  .person-name { font-weight: 600; font-size: 30px; color: var(--brand-red); letter-spacing: 2px; }
  .person-title { font-weight: 500; font-size: 19px; color: var(--ink); letter-spacing: 1.5px; margin-top: 4px; }
  .office-address { margin-top: 34px; font-size: 16px; line-height: 26px; color: var(--ink); letter-spacing: 1px; }
  .column-divider {
    position: absolute; left: 500px; top: 182px; width: 2px; height: 150px;
    background: var(--brand-grey); opacity: .6;
  }
  .contact-list {
    position: absolute; left: 522px; top: 186px;
    list-style: none; font-size: 17px; color: var(--ink); letter-spacing: 1px;
  }
  .contact-list li { display: flex; align-items: center; gap: 12px; height: 30px; }
  .contact-icon { width: 20px; height: 20px; flex: none; }
  .contact-list .email { font-size: 14px; letter-spacing: .3px; }
</style>
</head>
<body>
  <article class="business-card">
    <svg class="card-swoosh" viewBox="0 0 900 520" aria-hidden="true">
      <path d="M0 360 C 200 330, 420 420, 900 380 L900 520 L0 520 Z" fill="#bfc0c2"/>
      <path d="M0 352 C 220 318, 430 412, 900 366" fill="none" stroke="var(--brand-red)" stroke-width="9"/>
      <path d="M0 376 C 230 350, 450 436, 900 398" fill="none" stroke="var(--brand-red)" stroke-width="3"/>
      <path d="M0 400 C 240 380, 470 460, 900 430 L900 520 L0 520 Z" fill="#a9aaac"/>
    </svg>

    <div class="brand-name">HALVERN</div>

    <div class="identity">
      <div class="person-name">Dennis Whitlock</div>
      <div class="person-title">Director of Operations</div>
      <div class="office-address">6387 Larkmeadow Lane<br>Elk Grove, CA 95731</div>
    </div>

    <div class="column-divider"></div>

    <ul class="contact-list">
      <li><svg class="contact-icon" viewBox="0 0 20 20"><circle cx="10" cy="10" r="10" fill="var(--ink)"/><path d="M6.5 5.5l2 2-1 1.2c.6 1.4 1.6 2.4 3 3l1.2-1 2 2-1.2 1.6c-3.6-.4-6.8-3.6-7.2-7.2z" fill="#fff"/></svg>916-555-0142</li>
      <li><svg class="contact-icon" viewBox="0 0 20 20"><circle cx="10" cy="10" r="10" fill="var(--ink)"/><rect x="6.5" y="4.5" width="7" height="11" rx="1.2" fill="#fff"/><rect x="7.7" y="6" width="4.6" height="6.5" fill="var(--ink)"/></svg>916-555-0187</li>
      <li><svg class="contact-icon" viewBox="0 0 20 20"><circle cx="10" cy="10" r="10" fill="var(--ink)"/><rect x="5" y="8" width="10" height="6" fill="#fff"/><rect x="7" y="5" width="6" height="3" fill="#fff"/></svg>916-555-0163</li>
      <li><svg class="contact-icon" viewBox="0 0 20 20"><circle cx="10" cy="10" r="10" fill="var(--ink)"/><rect x="5" y="6.5" width="10" height="7" fill="#fff"/><path d="M5 6.5l5 4 5-4" fill="none" stroke="var(--ink)" stroke-width="1.2"/></svg><span class="email">dennis.whitlock@halvernbldg.com</span></li>
      <li><svg class="contact-icon" viewBox="0 0 20 20"><circle cx="10" cy="10" r="10" fill="var(--ink)"/><circle cx="10" cy="10" r="5" fill="none" stroke="#fff" stroke-width="1.3"/><path d="M5 10h10M10 5c-2 3-2 7 0 10M10 5c2 3 2 7 0 10" fill="none" stroke="#fff" stroke-width="1"/></svg>www.halvernbldg.com</li>
    </ul>
  </article>
</body>
</html>
```